Iron and home washing service

I provide I home iron and washing service for adult and kids clothes on a smoke pet free environment. I can collect and offer a next day delivery. Or same day depend on items and volume. I offer competitive frendly and reliable service and price. I charge by weight £4,50 / kg. approx 5 items =1 kg minimum for collection.

```html
<!DOCTYPE html>
<html lang="en">
<head>
<meta charset="UTF-8">
<title>Iron Service Flyer</title>
<link rel="stylesheet" href="https://fonts.googleapis.com/css2?family=Roboto+Condensed:wght@700;900&family=Open+Sans:wght@600;700&display=swap">
<style>
  :root {
    --pink: #e6007e;
    --pink-soft: #e95fa5;
    --blue: #1f8fd8;
    --blue-deep: #1a86cf;
    --blue-light: #35aee8;
    --ink: #3a3a3a;
    --white: #ffffff;
    --paper: #f4f6f9;
    --rule: #9a9a9a;
  }
  * { margin: 0; padding: 0; box-sizing: border-box; }
  html, body { width: 900px; height: 1200px; overflow: hidden; background: var(--white); }
  .flyer {
    position: relative;
    width: 900px;
    height: 1200px;
    overflow: hidden;
    background: linear-gradient(180deg, var(--white) 0%, var(--paper) 60%, #e9edf3 100%);
    font-family: "Open Sans", Arial, sans-serif;
  }
  .backdrop { position: absolute; inset: 0; width: 900px; height: 1200px; }
  .title {
    position: absolute;
    left: 56px;
    top: 382px;
    font-family: "Roboto Condensed", "Arial Narrow", sans-serif;
    font-weight: 900;
    font-size: 92px;
    letter-spacing: 1px;
    color: var(--pink);
    line-height: 1;
  }
  .intro {
    position: absolute;
    left: 56px;
    top: 530px;
    width: 230px;
    font-family: "Roboto Condensed", "Arial Narrow", sans-serif;
    font-weight: 700;
    font-size: 27px;
    line-height: 1.3;
    color: var(--blue);
  }
  .divider {
    position: absolute;
    left: 298px;
    top: 532px;
    width: 1px;
    height: 160px;
    background: var(--rule);
  }
  .price-list {
    position: absolute;
    left: 330px;
    top: 528px;
    list-style: none;
    font-weight: 700;
    font-size: 21px;
    line-height: 1.4;
    color: var(--ink);
  }
  .price-list li { position: relative; padding-left: 28px; margin-bottom: 9px; }
  .price-list li::before {
    content: "";
    position: absolute;
    left: 0;
    top: 8px;
    width: 13px;
    height: 13px;
    border-radius: 50%;
    background: var(--white);
    border: 4px solid var(--pink-soft);
    box-sizing: border-box;
  }
  .special-badge {
    position: absolute;
    left: 247px;
    top: 745px;
    width: 202px;
    height: 202px;
    border-radius: 50%;
    background: var(--white);
    box-shadow: 0 3px 10px rgba(0,0,0,0.15);
    display: flex;
    align-items: center;
    justify-content: center;
  }
  .special-badge span {
    width: 182px;
    height: 182px;
    border-radius: 50%;
    background: var(--pink-soft);
    color: var(--white);
    font-family: "Roboto Condensed", "Arial Narrow", sans-serif;
    font-weight: 700;
    font-size: 40px;
    line-height: 1.05;
    text-align: center;
    display: flex;
    align-items: center;
    justify-content: center;
    text-shadow: 0 2px 3px rgba(0,0,0,0.25);
  }
  .newborn-heading {
    position: absolute;
    left: 54px;
    top: 866px;
    width: 260px;
    font-family: "Roboto Condensed", "Arial Narrow", sans-serif;
    font-weight: 700;
    font-size: 26px;
    line-height: 1.25;
    color: var(--white);
    text-shadow: 0 1px 2px rgba(0,0,0,0.25);
  }
  .newborn-list {
    position: absolute;
    left: 60px;
    top: 1000px;
    list-style: none;
    font-weight: 600;
    font-size: 20px;
    line-height: 1.38;
    color: var(--white);
  }
  .newborn-list li { position: relative; padding-left: 32px; margin-bottom: 5px; }
  .newborn-list .tick {
    position: absolute;
    left: 0;
    top: 4px;
    width: 20px;
    height: 20px;
  }
  .photo-slot { position: absolute; }
</style>
</head>
<body>
<main class="flyer">
  <svg class="backdrop" viewBox="0 0 900 1200" aria-hidden="false">
    <defs>
      <linearGradient id="ironingPhotoTone" x1="0" y1="0" x2="1" y2="1">
        <stop offset="0" stop-color="#b9b9bb"/>
        <stop offset="0.45" stop-color="#e8e9ea"/>
        <stop offset="1" stop-color="#cfd6cf"/>
      </linearGradient>
      <linearGradient id="blueField" x1="0" y1="0" x2="0" y2="1">
        <stop offset="0" stop-color="#3aaee6"/>
        <stop offset="1" stop-color="#1a86cf"/>
      </linearGradient>
      <linearGradient id="motherPhotoTone" x1="0" y1="0" x2="1" y2="1">
        <stop offset="0" stop-color="#c9a48f"/>
        <stop offset="0.5" stop-color="#f0d9cf"/>
        <stop offset="1" stop-color="#e9c3c7"/>
      </linearGradient>
      <linearGradient id="laundryTone" x1="0" y1="0" x2="1" y2="0">
        <stop offset="0" stop-color="#dfeefa"/>
        <stop offset="1" stop-color="#f6b7cf"/>
      </linearGradient>
    </defs>

    <!-- header photo area -->
    <path role="img" aria-label="Photo: hand pressing a white iron on a shirt beside a pile of folded clothes"
          d="M0,0 H900 V350 C700,352 430,330 260,280 C160,248 70,205 0,178 Z"
          fill="url(#ironingPhotoTone)"/>
    <path d="M0,178 C70,205 160,248 260,280 C430,330 700,352 900,350 V372 C700,372 430,350 255,300 C150,268 60,222 0,200 Z" fill="var(--pink)"/>
    <path d="M0,200 C60,222 150,268 255,300 C430,350 700,372 900,372 V385 C700,385 430,362 250,312 C145,280 55,232 0,212 Z" fill="var(--blue-light)"/>

    <!-- lower blue field with curved stripes -->
    <path d="M0,690 C130,760 290,840 560,880 L900,880 V1200 H0 Z" fill="var(--blue-light)"/>
    <path d="M0,712 C130,782 290,860 560,900 L900,900 V1200 H0 Z" fill="var(--pink)"/>
    <path d="M0,730 C130,800 290,876 560,914 L900,914 V1200 H0 Z" fill="var(--white)"/>
    <path d="M0,744 C130,814 290,888 560,926 L900,926 V1200 H0 Z" fill="url(#blueField)"/>

    <!-- heart-shaped photo frame -->
    <path d="M535,1200 C470,1080 455,900 484,815 C510,755 565,735 630,738 C700,742 745,778 790,782 C840,778 870,752 900,745 V1200 Z" fill="#d5d7da"/>
    <path d="M543,1200 C478,1080 466,900 494,822 C520,766 570,748 630,751 C700,755 742,790 790,794 C840,790 870,766 900,758 V1200 Z" fill="var(--pink)"/>
    <path role="img" aria-label="Photo: mother holding a newborn baby"
          d="M553,1200 C490,1080 478,904 505,830 C530,776 575,760 630,763 C698,767 740,802 790,806 C840,802 870,780 900,772 V1200 Z"
          fill="url(#motherPhotoTone)"/>

    <!-- small laundry still life -->
    <rect role="img" aria-label="Illustration: steam iron beside a stack of colourful folded towels"
          x="400" y="1042" width="190" height="118" rx="14" fill="url(#laundryTone)" opacity="0.92"/>
  </svg>

  <h1 class="title">IRON SERVICE</h1>

  <p class="intro">With the option do drop and collect by Customer Price</p>
  <div class="divider"></div>
  <ul class="price-list">
    <li>£8 pounds for 10 garments</li>
    <li>£20 pounds 25 garments</li>
    <li>Optional wash and ironing please ask price</li>
    <li>Collection and delivery free on<br>£25 pounds order</li>
  </ul>

  <div class="special-badge"><span>SPECIAL<br>SERVICE</span></div>

  <h2 class="newborn-heading">Welcome<br>Your Newborn<br>Baby for Busy<br>Mothers</h2>

  <ul class="newborn-list">
    <li><svg class="tick" viewBox="0 0 20 20"><rect x="1" y="3" width="16" height="16" rx="3" fill="#fff"/><path d="M4,10 L8,14 L18,2" fill="none" stroke="#e6007e" stroke-width="3.5" stroke-linecap="round" stroke-linejoin="round"/></svg>Washing and Iron</li>
    <li><svg class="tick" viewBox="0 0 20 20"><rect x="1" y="3" width="16" height="16" rx="3" fill="#fff"/><path d="M4,10 L8,14 L18,2" fill="none" stroke="#e6007e" stroke-width="3.5" stroke-linecap="round" stroke-linejoin="round"/></svg>Sterlised on vaccum sealed<br>bag to avoid contamination</li>
    <li><svg class="tick" viewBox="0 0 20 20"><rect x="1" y="3" width="16" height="16" rx="3" fill="#fff"/><path d="M4,10 L8,14 L18,2" fill="none" stroke="#e6007e" stroke-width="3.5" stroke-linecap="round" stroke-linejoin="round"/></svg><strong>Price £20 pounds for<br>30 garments</strong></li>
    <li><svg class="tick" viewBox="0 0 20 20"><rect x="1" y="3" width="16" height="16" rx="3" fill="#fff"/><path d="M4,10 L8,14 L18,2" fill="none" stroke="#e6007e" stroke-width="3.5" stroke-linecap="round" stroke-linejoin="round"/></svg>Collection and delivery free</li>
  </ul>
</main>
</body>
</html>
```